Need a Crisps (Potato Chips in US) and Popcorns Logo, Artwork and Packaging Design

I want to package my home made crisps and popcorns. The crisps will be going by the name ZapZop (Ks are capital) and the popcorns by the name munbuns (Should all be in same case, either all small or all caps - I leave it to designer's choice).

Crisps:
I want both a logo that will be associated with the product and a package design with the logo embedded. The logo should be playful and striking.

The packaging for the crisps should be to the standards of international brands like Tavo, Wumbles, Flindas, etc. Package type is the pouch based packages.

The colours should be vibrant. We are limited to 4 colours in the design due to printing costs. So the designer should use a mixture that is striking especially to children and young adults.

Incorporation of animal artwork is allowed as long as it does not infringe on IPs.

Popcorns:
This one is less intensive and only requires a logo and package design like the one used in movie halls.

Target Market(s)

Kids and young adults

Industry/Entity Type

Food Production

Logo Text

ZapZop for crisps and munbuns for popcorn

Colors

Designer to choose colors to be used in the design.

Requirements
Must have
• Playful font and colours
Nice to have
• Distinguishing artwork

```html
<!DOCTYPE html>
<html lang="en">
<head>
<meta charset="utf-8">
<title>ZapZop Crisps – Pouch Designs</title>
<link href="https://fonts.googleapis.com/css2?family=Open+Sans:wght@400;600&display=swap" rel="stylesheet">
<style>
  :root{
    --page-light:#fff8c4;
    --page-warm:#fbd79a;
    --page-deep:#f08a5a;
    --brand-blue:#0b1cf2;
    --brand-blue-light:#2aa8e2;
    --brand-orange:#ff4a00;
    --brand-yellow:#ffff00;
    --brand-red:#ff1a00;
    --band-blue-dark:#14149a;
    --band-red-dark:#a01000;
    --swatch-grey:#b3b3b3;
    --ink:#111111;
    --white:#ffffff;
    --chips-light:#f6e7b0;
    --chips-warm:#e8b86a;
  }
  *{margin:0;padding:0;box-sizing:border-box}
  html,body{width:1200px;height:1200px;overflow:hidden}
  body{
    position:relative;
    font-family:"Open Sans",sans-serif;
    background:radial-gradient(ellipse 70% 70% at 50% 50%, var(--page-light) 0%, var(--page-warm) 55%, var(--page-deep) 110%);
  }
  .pouch{position:absolute}
  .pouch svg.pouch-shape{position:absolute;left:0;top:0}
  .band{position:absolute;left:0;width:100%}
  .pouch--blue{left:51px;top:105px;width:558px;height:732px}
  .pouch--blue .band{background:repeating-linear-gradient(var(--band-blue-dark) 0 2px,var(--brand-blue) 2px 4px)}
  .pouch--blue .band--top{top:0;height:23px}
  .pouch--blue .band--bottom{top:707px;height:25px}
  .pouch--sun{left:697px;top:464px;width:420px;height:550px}
  .pouch--sun .band{background:repeating-linear-gradient(var(--band-red-dark) 0 2px,var(--brand-red) 2px 4px)}
  .pouch--sun .band--top{top:0;height:18px}
  .pouch--sun .band--bottom{top:534px;height:16px}

  .price{position:absolute;line-height:1}
  .pouch--blue .price{right:10px;top:60px;font-size:32px;color:var(--ink)}
  .pouch--sun .price{right:8px;top:44px;font-size:23px;color:var(--white)}

  .logo-plate{
    position:absolute;display:flex;align-items:center;justify-content:center;
    border-radius:0 30px 0 30px;
  }
  .logo-name{font-weight:600;color:var(--brand-yellow);line-height:1;letter-spacing:1px}
  .pouch--blue .logo-plate{left:63px;top:190px;width:432px;height:143px;background:var(--brand-orange);box-shadow:0 0 14px 4px rgba(255,255,255,.75)}
  .pouch--blue .logo-name{font-size:98px}
  .pouch--sun .logo-plate{left:47px;top:143px;width:325px;height:107px;background:var(--brand-blue);box-shadow:0 0 10px 3px rgba(255,255,255,.7)}
  .pouch--sun .logo-name{font-size:74px}

  .flavour{position:absolute;line-height:1}
  .pouch--blue .flavour{left:103px;top:345px;font-size:30px;color:var(--white)}
  .pouch--sun .flavour{left:79px;top:258px;font-size:22px;color:var(--ink)}

  .snack-visual{position:absolute;border-radius:45% 45% 40% 40%}
  .pouch--blue .snack-visual{left:40px;top:388px;width:464px;height:284px;background:radial-gradient(ellipse at 50% 65%, var(--chips-light) 0%, var(--chips-warm) 45%, rgba(232,184,106,0) 72%)}
  .pouch--sun .snack-visual{left:27px;top:284px;width:352px;height:212px;background:radial-gradient(ellipse at 50% 65%, var(--chips-light) 0%, var(--chips-warm) 45%, rgba(232,184,106,0) 72%)}

  .swatch{position:absolute;left:25px;width:245px;height:80px}
  .swatch .logo-plate{left:22px;top:10px;width:201px;height:66px;border-radius:0 22px 0 22px}
  .swatch .logo-name{font-size:46px}
  .swatch--orange{top:864px;background:var(--brand-orange)}
  .swatch--orange .logo-plate{background:var(--brand-blue)}
  .swatch--blue{top:950px;background:var(--brand-blue)}
  .swatch--blue .logo-plate{background:var(--brand-orange)}
  .swatch--white{top:1035px;background:var(--white)}
  .swatch--white .logo-plate{background:var(--swatch-grey)}
  .swatch--white .logo-name{color:var(--white)}
  .swatch--black{top:1120px;background:var(--ink)}
  .swatch--black .logo-plate{background:var(--swatch-grey)}
  .swatch--black .logo-name{color:var(--ink)}
</style>
</head>
<body>

<section class="pouch pouch--blue">
  <svg class="pouch-shape" width="558" height="732" viewBox="0 0 558 732">
    <defs>
      <radialGradient id="blue-glow" cx="0.5" cy="0.55" r="0.55">
        <stop offset="0" stop-color="var(--brand-blue-light)"/>
        <stop offset="1" stop-color="var(--brand-blue)"/>
      </radialGradient>
    </defs>
    <rect x="0" y="0" width="558" height="732" fill="var(--brand-yellow)"/>
    <path d="M0,116 Q0,23 69,23 L359,23 C460,23 545,150 558,271 L558,732 L0,732 Z" fill="url(#blue-glow)"/>
  </svg>
  <div class="band band--top"></div>
  <div class="band band--bottom"></div>
  <span class="price">Rs.10</span>
  <div class="logo-plate"><span class="logo-name">ZapZop</span></div>
  <span class="flavour">Spicey</span>
  <div class="snack-visual" role="img" aria-label="Photo of potato crisps with red chillies and sliced sweet potato"></div>
</section>

<section class="pouch pouch--sun">
  <svg class="pouch-shape" width="420" height="550" viewBox="0 0 420 550">
    <defs>
      <radialGradient id="sun-glow" cx="0.55" cy="0.55" r="0.6">
        <stop offset="0" stop-color="var(--brand-yellow)"/>
        <stop offset="0.45" stop-color="var(--brand-yellow)"/>
        <stop offset="0.8" stop-color="#ff9a00"/>
        <stop offset="1" stop-color="var(--brand-red)"/>
      </radialGradient>
    </defs>
    <rect x="0" y="0" width="420" height="550" fill="var(--brand-blue)"/>
    <path d="M0,72 Q0,18 63,18 L263,18 C350,18 410,110 420,192 L420,550 L0,550 Z" fill="url(#sun-glow)"/>
  </svg>
  <div class="band band--top"></div>
  <div class="band band--bottom"></div>
  <span class="price">Rs.10</span>
  <div class="logo-plate"><span class="logo-name">ZapZop</span></div>
  <span class="flavour">Spicey</span>
  <div class="snack-visual" role="img" aria-label="Photo of potato crisps with red chillies and sliced sweet potato"></div>
</section>

<div class="swatch swatch--orange"><div class="logo-plate"><span class="logo-name">ZapZop</span></div></div>
<div class="swatch swatch--blue"><div class="logo-plate"><span class="logo-name">ZapZop</span></div></div>
<div class="swatch swatch--white"><div class="logo-plate"><span class="logo-name">ZapZop</span></div></div>
<div class="swatch swatch--black"><div class="logo-plate"><span class="logo-name">ZapZop</span></div></div>

</body>
</html>
```